Glow & Gloss by Mina
Text 410.582.3107 to set up and appointment
Instagram is Glow_GlossByMina
Location 4318 Fernwick Rd. Notthingham Md, 21087 Suit 204
Slogan "Flawless Blends. Beautiful You.
Specializing in pressicion cuts, blonding, fades, perms, waxing and more

The salon is black, gun metal color mirror with led lights. Green plants and has natural wood countertops for accent colors. Modern yet elegant. I want the card simple but it needs something to really grab the clients attention. I like black, grey, gold, green, natural tones and hints of pink or gold coloring
I’m open to anything. I don’t have a logo. Suggestions are welcome

Target Market(s)

20-60 men and woman

Industry/Entity Type

Hairstylist / barber

Contact Information for Business Card

The name of the show should be bold. Maybe the letters could raised I also like foil for shine added or a mat finish

Colors

Designer to choose colors to be used in the design.

Requirements
Must have
• I also like some floral Floral designs, but not too overpowering. I like Sparkle, Watercolor design, Or a geometric line in the background
Nice to have
• I’m really here because I need creative help. I’m open for suggestions. I’ll post a picture of the salon in inspiration if I can find it.
Should not have
• Checkered background

```html
<!DOCTYPE html>
<html lang="en">
<head>
<meta charset="utf-8">
<title>Glow &amp; Gloss by Mina – Business Card</title>
<link href="https://fonts.googleapis.com/css2?family=Source+Sans+3:wght@400&family=Playfair+Display:wght@400&display=swap" rel="stylesheet">
<style>
  :root {
    --gold: #b99b6b;
    --gold-glow: rgba(185, 155, 107, 0.42);
    --gold-fade: rgba(185, 155, 107, 0.12);
    --silk-deep: #050607;
    --silk-mid: #1b1e21;
    --silk-sheen: rgba(61, 65, 70, 0.55);
    --paper: #ffffff;
  }
  * { margin: 0; padding: 0; box-sizing: border-box; }
  html, body {
    width: 902px;
    height: 1200px;
    overflow: hidden;
    background: var(--paper);
    font-family: "Source Sans 3", "Myriad Pro", sans-serif;
  }
  .canvas { position: relative; width: 902px; height: 1200px; }

  .card-side {
    position: absolute;
    left: 0;
    width: 902px;
    height: 571px;
    overflow: hidden;
    background:
      linear-gradient(160deg, transparent 30%, var(--silk-sheen) 42%, transparent 52%),
      linear-gradient(200deg, transparent 55%, rgba(61,65,70,0.45) 66%, transparent 78%),
      linear-gradient(170deg, var(--silk-deep) 0%, var(--silk-mid) 35%, var(--silk-deep) 50%, var(--silk-mid) 72%, var(--silk-deep) 100%);
  }
  .card-front { top: 0; }
  .card-back { top: 630px; }

  .gold-frame {
    position: absolute;
    border: 3px solid var(--gold);
  }
  .card-front .gold-frame { left: 37px; top: 51px; width: 827px; height: 472px; }
  .card-back .gold-frame { left: 39px; top: 51px; width: 827px; height: 471px; }

  .corner-ornament {
    position: absolute;
    width: 150px;
    height: 140px;
    pointer-events: none;
  }
  .card-front .corner-ornament {
    left: 719px; top: 388px;
    background: radial-gradient(ellipse farthest-side at 100% 100%, var(--gold-glow) 0%, var(--gold-fade) 55%, transparent 100%);
  }
  .card-back .corner-ornament {
    left: 34px; top: 46px;
    background: radial-gradient(ellipse farthest-side at 0% 0%, var(--gold-glow) 0%, var(--gold-fade) 55%, transparent 100%);
  }

  .appointment-heading {
    position: absolute;
    left: 113px;
    top: 141px;
    font-size: 48px;
    font-weight: 400;
    letter-spacing: -1.5px;
    color: var(--gold);
    line-height: 1;
    white-space: nowrap;
  }
  .heading-rule {
    position: absolute;
    left: 105px;
    top: 203px;
    width: 475px;
    height: 2px;
    background: var(--gold);
  }

  .contact-row { position: absolute; left: 112px; display: flex; align-items: center; gap: 24px; color: var(--gold); white-space: nowrap; }
  .contact-row svg { width: 45px; height: 45px; flex: none; }
  .row-phone { top: 238px; font-size: 34px; letter-spacing: 0.5px; }
  .row-social { top: 312px; font-size: 30px; }
  .row-address { top: 386px; font-size: 20px; line-height: 27px; }

  .brand-lockup {
    position: absolute;
    left: 0;
    right: 0;
    top: 186px;
    text-align: center;
    color: var(--gold);
    font-family: "Playfair Display", "Bodoni 72", serif;
    font-weight: 400;
  }
  .brand-mark {
    width: 46px;
    height: 46px;
    margin: 0 auto 18px;
    border: 3px solid var(--gold);
    border-radius: 50%;
  }
  .brand-name { font-size: 54px; letter-spacing: 1px; line-height: 1; white-space: nowrap; }
  .brand-byline {
    display: flex;
    align-items: center;
    justify-content: center;
    gap: 12px;
    margin-top: 6px;
    font-size: 30px;
    line-height: 1;
  }
  .byline-rule { width: 112px; height: 2px; background: var(--gold); }
</style>
</head>
<body>
<main class="canvas">

  <section class="card-side card-front" aria-label="Card front">
    <div class="gold-frame"></div>
    <div class="corner-ornament" role="img" aria-label="Gold floral corner flourish"></div>

    <h2 class="appointment-heading">TEXT FOR APPOINTMENT:</h2>
    <div class="heading-rule"></div>

    <div class="contact-row row-phone">
      <svg viewBox="0 0 44 44" aria-hidden="true">
        <rect x="2" y="2" width="40" height="40" rx="9" fill="none" stroke="#b99b6b" stroke-width="3.5"/>
        <path d="M14 11c2-1 4 4 4 6s-2 2-1 4c1 3 4 6 7 7 2 1 2-1 4-1s7 2 6 4c-1 3-4 4-6 3-7-2-13-8-15-15-1-3 0-7 1-8z" fill="none" stroke="#b99b6b" stroke-width="3" stroke-linejoin="round"/>
      </svg>
      <span>410.582.3107</span>
    </div>

    <div class="contact-row row-social">
      <svg viewBox="0 0 44 44" aria-hidden="true">
        <circle cx="22" cy="22" r="19.5" fill="none" stroke="#b99b6b" stroke-width="3.5"/>
      </svg>
      <span>@Glow_GlossByMina</span>
    </div>

    <div class="contact-row row-address">
      <svg viewBox="0 0 44 44" aria-hidden="true">
        <rect x="2" y="2" width="40" height="40" rx="9" fill="none" stroke="#b99b6b" stroke-width="3.5"/>
        <path d="M22 33c-5-6-8-10-8-14a8 8 0 0 1 16 0c0 4-3 8-8 14z" fill="none" stroke="#b99b6b" stroke-width="3"/>
        <circle cx="22" cy="19" r="3" fill="none" stroke="#b99b6b" stroke-width="2.5"/>
        <path d="M13 34h18" stroke="#b99b6b" stroke-width="2.5" stroke-linecap="round"/>
      </svg>
      <span>4318 Fernwick Rd. Nottingham Md,<br>21087 Suit 204</span>
    </div>
  </section>

  <section class="card-side card-back" aria-label="Card back">
    <div class="gold-frame"></div>
    <div class="corner-ornament" role="img" aria-label="Gold floral corner flourish"></div>

    <div class="brand-lockup">
      <div class="brand-mark"></div>
      <div class="brand-name">GLOW &amp; GLOSS</div>
      <div class="brand-byline">
        <span class="byline-rule"></span>
        <span>by Mina</span>
        <span class="byline-rule"></span>
      </div>
    </div>
  </section>

</main>
</body>
</html>
```